Higher co-efficient of performance means more heat for your money

I need a bar graph that will have the following heating systems, 80% efficient gas furnace COP of .8, Electric heat COP of 1, and Our best selling heat pump with a cop of 4 at 47F. I will have a constant bar, 100$ worth of gas for furnace, 100$ of electricity for electric heat, and 100$ worth of electricity for our heat pumps. next to them I will have a bar showing how much heat each heating system will provide for $100 of fuel. For gas furnace I need a bar that says $80 worth of heat and the barograph to match it, for electric heat I need the bar to show 100$ worth of heat, for our best selling heat pump I need the bar graph to show and say $400 dollars worth of heat. Please take a look at my website www.summitbreezecomfort.example for brand color and feel

```html
<!DOCTYPE html>
<html lang="en">
<head>
<meta charset="utf-8">
<title>More Heat for Your Money</title>
<link rel="stylesheet" href="https://fonts.googleapis.com/css2?family=Montserrat:ital,wght@0,400;0,600;0,700;1,400&display=swap">
<style>
  :root {
    --brand-red: #c8262e;
    --brand-blue: #0c6fbf;
    --ink: #222222;
    --muted: #444444;
    --panel-grey: #e8e8ea;
    --grid: #c9c9cc;
    --bar-blue: #0070bc;
    --bar-red: #c1272d;
    --marker-grey: #a5a5a5;
  }
  html, body {
    margin: 0;
    padding: 0;
    width: 1200px;
    height: 2247px;
    overflow: hidden;
    background: #ffffff;
    font-family: "Montserrat", Arial, sans-serif;
  }
  .infographic { display: block; width: 1200px; height: 1123.5px; }
  .title-lead { font-size: 17px; font-weight: 700; fill: var(--ink); }
  .title-main { font-size: 24px; font-weight: 700; }
  .title-red { fill: var(--brand-red); }
  .title-blue { fill: var(--brand-blue); }
  .brand-name { font-size: 8.6px; font-weight: 700; fill: var(--brand-blue); letter-spacing: 0.3px; }
  .brand-mark { fill: var(--brand-red); }
  .footnote { font-size: 12px; font-style: italic; fill: var(--muted); }
  .grid-line { stroke: var(--grid); stroke-width: 0.8; }
  .axis-line { stroke: #3a3a3a; stroke-width: 1; }
  .amount { font-size: 16.5px; font-weight: 700; fill: var(--ink); }
  .amount-caption { font-size: 12px; fill: var(--muted); }
  .category { font-size: 13.5px; fill: var(--muted); }
  .category-strong { font-weight: 700; fill: var(--ink); }
  .flow-marker { fill: var(--marker-grey); }
  .flow-arc { fill: none; stroke-width: 1.4; }
  .flow-arc-blend { stroke: url(#arcBlend); }
  .flow-arc-red { stroke: var(--brand-red); }
  .flow-arc-plain { stroke: var(--bar-red); }
</style>
</head>
<body>

<!-- Gradient variant -->
<svg class="infographic infographic--gradient" viewBox="0 0 721 675" role="img" aria-label="Bar chart comparing heat delivered per 100 dollars of fuel">
  <defs>
    <linearGradient id="barBlueGradient" x1="0" y1="0" x2="0" y2="1">
      <stop offset="0" stop-color="#2f78bb"/>
      <stop offset="1" stop-color="#2c4a8a"/>
    </linearGradient>
    <linearGradient id="barRedGradient" x1="0" y1="0" x2="0" y2="1">
      <stop offset="0" stop-color="#ff6f72"/>
      <stop offset="0.45" stop-color="#ef3a33"/>
      <stop offset="1" stop-color="#e52a22"/>
    </linearGradient>
    <linearGradient id="arcBlend" x1="0" y1="0" x2="1" y2="0">
      <stop offset="0" stop-color="#2c5190"/>
      <stop offset="1" stop-color="#c8262e"/>
    </linearGradient>
    <marker id="headRed" viewBox="0 0 10 10" refX="6" refY="5" markerWidth="7" markerHeight="7" orient="auto">
      <path d="M0 0 L10 5 L0 10 Z" fill="#c8262e"/>
    </marker>
    <marker id="headPlain" viewBox="0 0 10 10" refX="6" refY="5" markerWidth="7" markerHeight="7" orient="auto">
      <path d="M0 0 L10 5 L0 10 Z" fill="#c1272d"/>
    </marker>
  </defs>

  <rect class="panel" x="0" y="0" width="705" height="675" fill="var(--panel-grey)"/>

  <text class="title-lead" x="72" y="77">Higher Co-efficient of Performance means</text>
  <text class="title-main" x="72" y="107"><tspan class="title-red">More Heat for </tspan><tspan class="title-blue">Your Money</tspan></text>

  <g class="brand">
    <rect class="brand-mark" x="599" y="57" width="20" height="20"/>
    <text class="brand-name" x="609" y="94" text-anchor="middle">SUMMIT BREEZE</text>
    <text class="brand-name" x="609" y="105" text-anchor="middle">COMFORT</text>
  </g>

  <text class="footnote" x="72" y="194">*COP measure at 47°F</text>

  <g class="grid">
    <line class="grid-line" x1="72" y1="209" x2="650" y2="209"/>
    <line class="grid-line" x1="72" y1="299" x2="650" y2="299"/>
    <line class="grid-line" x1="72" y1="388" x2="650" y2="388"/>
    <line class="grid-line" x1="72" y1="478" x2="650" y2="478"/>
  </g>

  <g class="bars">
    <rect x="72" y="478" width="58" height="90" fill="url(#barBlueGradient)"/>
    <rect x="151" y="490" width="58" height="78" fill="url(#barRedGradient)"/>
    <rect x="292" y="478" width="58" height="90" fill="url(#barBlueGradient)"/>
    <rect x="371" y="478" width="58" height="90" fill="url(#barRedGradient)"/>
    <rect x="512" y="478" width="58" height="90" fill="url(#barBlueGradient)"/>
    <rect x="591" y="209" width="58" height="359" fill="url(#barRedGradient)"/>
    <path class="flow-marker" d="M137 518 L146 523 L137 528 Z"/>
    <path class="flow-marker" d="M357 518 L366 523 L357 528 Z"/>
    <path class="flow-marker" d="M577 518 L586 523 L577 528 Z"/>
  </g>
  <line class="axis-line" x1="72" y1="568" x2="650" y2="568"/>

  <g class="flows">
    <path class="flow-arc flow-arc-blend" d="M99 398 C108 360 168 358 180 402" marker-end="url(#headRed)"/>
    <path class="flow-arc flow-arc-blend" d="M319 398 C328 360 388 358 400 402" marker-end="url(#headRed)"/>
    <path class="flow-arc flow-arc-red" d="M538 400 L538 175 Q538 157 556 157 L584 157" marker-end="url(#headRed)"/>
  </g>

  <g class="amounts" text-anchor="middle">
    <text class="amount" x="99" y="437">100$</text>
    <text class="amount-caption" x="99" y="450">worth</text>
    <text class="amount-caption" x="99" y="466">of Gas</text>
    <text class="amount" x="180" y="437">80$</text>
    <text class="amount-caption" x="180" y="450">worth</text>
    <text class="amount-caption" x="180" y="466">of Heat</text>
    <text class="amount" x="319" y="437">100$</text>
    <text class="amount-caption" x="319" y="450">worth</text>
    <text class="amount-caption" x="319" y="466">of Gas</text>
    <text class="amount" x="400" y="437">100$</text>
    <text class="amount-caption" x="400" y="450">worth</text>
    <text class="amount-caption" x="400" y="466">of Heat</text>
    <text class="amount" x="541" y="437">100$</text>
    <text class="amount-caption" x="541" y="450">worth</text>
    <text class="amount-caption" x="541" y="466">of Gas</text>
    <text class="amount" x="620" y="165">400$</text>
    <text class="amount-caption" x="620" y="181">worth</text>
    <text class="amount-caption" x="620" y="196">of Heat</text>
  </g>

  <g class="categories" text-anchor="middle">
    <text class="category" x="140" y="597">80%</text>
    <text class="category" x="140" y="615">Gas Funace</text>
    <text class="category" x="361" y="597">Electric</text>
    <text class="category" x="361" y="615">Heat</text>
    <text class="category category-strong" x="583" y="597">Our Best Selling</text>
    <text class="category category-strong" x="583" y="615">Heat Pump</text>
  </g>
</svg>

<!-- Flat variant -->
<svg class="infographic infographic--flat" viewBox="0 0 721 675" role="img" aria-label="Bar chart comparing heat delivered per 100 dollars of fuel">
  <text class="title-lead" x="72" y="77">Higher Co-efficient of Performance means</text>
  <text class="title-main" x="72" y="107"><tspan class="title-red">More Heat for </tspan><tspan class="title-blue">Your Money</tspan></text>

  <g class="brand">
    <rect class="brand-mark" x="599" y="57" width="20" height="20"/>
    <text class="brand-name" x="609" y="94" text-anchor="middle">SUMMIT BREEZE</text>
    <text class="brand-name" x="609" y="105" text-anchor="middle">COMFORT</text>
  </g>

  <text class="footnote" x="72" y="194">*COP measure at 47°F</text>

  <g class="grid">
    <line class="grid-line" x1="72" y1="209" x2="650" y2="209"/>
    <line class="grid-line" x1="72" y1="299" x2="650" y2="299"/>
    <line class="grid-line" x1="72" y1="388" x2="650" y2="388"/>
    <line class="grid-line" x1="72" y1="478" x2="650" y2="478"/>
  </g>

  <g class="bars">
    <rect x="72" y="478" width="58" height="90" fill="var(--bar-blue)"/>
    <rect x="151" y="490" width="58" height="78" fill="var(--bar-red)"/>
    <rect x="292" y="478" width="58" height="90" fill="var(--bar-blue)"/>
    <rect x="371" y="478" width="58" height="90" fill="var(--bar-red)"/>
    <rect x="512" y="478" width="58" height="90" fill="var(--bar-blue)"/>
    <rect x="591" y="209" width="58" height="359" fill="var(--bar-red)"/>
    <path class="flow-marker" d="M137 518 L146 523 L137 528 Z"/>
    <path class="flow-marker" d="M357 518 L366 523 L357 528 Z"/>
    <path class="flow-marker" d="M577 518 L586 523 L577 528 Z"/>
  </g>
  <line class="axis-line" x1="72" y1="568" x2="650" y2="568"/>

  <g class="flows">
    <path class="flow-arc flow-arc-blend" d="M99 398 C108 360 168 358 180 402" marker-end="url(#headPlain)"/>
    <path class="flow-arc flow-arc-blend" d="M319 398 C328 360 388 358 400 402" marker-end="url(#headPlain)"/>
    <path class="flow-arc flow-arc-plain" d="M538 400 L538 175 Q538 157 556 157 L584 157" marker-end="url(#headPlain)"/>
  </g>

  <g class="amounts" text-anchor="middle">
    <text class="amount" x="99" y="437">100$</text>
    <text class="amount-caption" x="99" y="450">worth</text>
    <text class="amount-caption" x="99" y="466">of Gas</text>
    <text class="amount" x="180" y="437">80$</text>
    <text class="amount-caption" x="180" y="450">worth</text>
    <text class="amount-caption" x="180" y="466">of Heat</text>
    <text class="amount" x="319" y="437">100$</text>
    <text class="amount-caption" x="319" y="450">worth</text>
    <text class="amount-caption" x="319" y="466">of Gas</text>
    <text class="amount" x="400" y="437">100$</text>
    <text class="amount-caption" x="400" y="450">worth</text>
    <text class="amount-caption" x="400" y="466">of Heat</text>
    <text class="amount" x="541" y="437">100$</text>
    <text class="amount-caption" x="541" y="450">worth</text>
    <text class="amount-caption" x="541" y="466">of Gas</text>
    <text class="amount" x="620" y="165">400$</text>
    <text class="amount-caption" x="620" y="181">worth</text>
    <text class="amount-caption" x="620" y="196">of Heat</text>
  </g>

  <g class="categories" text-anchor="middle">
    <text class="category" x="140" y="597">80%</text>
    <text class="category" x="140" y="615">Gas Funace</text>
    <text class="category" x="361" y="597">Electric</text>
    <text class="category" x="361" y="615">Heat</text>
    <text class="category category-strong" x="583" y="597">Our Best Selling</text>
    <text class="category category-strong" x="583" y="615">Heat Pump</text>
  </g>
</svg>

</body>
</html>
```